Robotic Physical Therapy office needs a Grand Opening Flyer

We need a Grand Opening flyer design for a robotic physical therapy office named Stellar Motion Therapy. We would like it to have a clean, classy, upscale feeling that gives potential clients a V.I.P. feeling. We would like to use the colors black, gray, and yellow (logo will be uploaded).

Event: Thursday, June 1st, 2023 from 12pm-6pm
location: 58274 Harlow Ave, Bloomfield Hills, MI 48319

Industry/Entity Type

Physical therapy

Font styles to use
Script

Colors

Designer to choose colors to be used in the design.

Requirements
Nice to have
• More of a vip feel for the invite

```html
<!DOCTYPE html>
<html lang="en">
<head>
<meta charset="utf-8">
<title>Grand Opening – Stellar Motion Therapy</title>
<link rel="stylesheet" href="https://fonts.googleapis.com/css2?family=Great+Vibes&family=Montserrat:ital,wght@0,700;0,800;0,900;1,500&family=Oswald:wght@600&display=swap">
<style>
  :root {
    --cream: #fbf3e2;
    --cream-deep: #f1dfbd;
    --white: #fffdf8;
    --gold: #b8741a;
    --gold-light: #e6b44a;
    --gold-dark: #6e420c;
    --ink: #2b2e3b;
    --ribbon-a: #f4d46a;
    --ribbon-b: #c98a1c;
    --photo-a: #eee9e2;
    --photo-b: #d8cfc4;
  }
  * { box-sizing: border-box; margin: 0; padding: 0; }
  html, body { width: 816px; height: 1200px; overflow: hidden; background: var(--white); }
  .flyer {
    position: relative;
    width: 816px; height: 1200px; overflow: hidden;
    background:
      radial-gradient(ellipse 60% 40% at 30% 30%, var(--white) 0%, transparent 70%),
      radial-gradient(ellipse 50% 60% at 80% 60%, var(--white) 0%, transparent 70%),
      linear-gradient(160deg, var(--cream) 0%, var(--white) 45%, var(--cream-deep) 100%);
    font-family: "Montserrat", sans-serif;
  }
  .gold-text {
    background: linear-gradient(180deg, var(--gold-light) 0%, var(--gold) 50%, var(--gold-dark) 100%);
    -webkit-background-clip: text; background-clip: text;
    color: transparent;
  }
  .ribbon {
    position: absolute;
    background: linear-gradient(135deg, var(--ribbon-a), var(--ribbon-b));
    opacity: 0.55;
    border-radius: 40% 60% 50% 50%;
  }
  .ribbon--top-left { left: 0; top: 14px; width: 230px; height: 100px; }
  .ribbon--top-right { left: 560px; top: 0; width: 256px; height: 198px; border-radius: 0 0 0 80%; }
  .ribbon--bottom-left { left: 0; top: 1050px; width: 211px; height: 150px; border-radius: 0 80% 0 0; }
  .ribbon--bottom-right { left: 566px; top: 998px; width: 250px; height: 192px; border-radius: 80% 0 0 40%; }
  .photo {
    position: absolute; left: 0; top: 742px; width: 760px; height: 458px;
    background: linear-gradient(120deg, var(--photo-a), var(--photo-b));
    -webkit-mask-image: linear-gradient(180deg, transparent 0%, #000 35%);
    mask-image: linear-gradient(180deg, transparent 0%, #000 35%);
  }
  .brand {
    position: absolute; left: 0; top: 106px; width: 816px; z-index: 2;
    display: flex; justify-content: center; align-items: center; gap: 10px;
  }
  .brand__mark { width: 30px; height: 30px; border-radius: 50%; background: var(--ink); }
  .brand__name { font-weight: 800; font-size: 22px; color: var(--ink); letter-spacing: 0.5px; }
  .headline {
    position: absolute; left: 0; width: 816px; text-align: center;
  }
  .headline--script {
    top: 140px; font-family: "Great Vibes", cursive; font-size: 190px; line-height: 1.25;
    padding: 0 40px 40px; font-weight: 400;
  }
  .headline--block {
    top: 350px; font-family: "Montserrat", sans-serif; font-weight: 900; font-size: 66px; line-height: 1.1; letter-spacing: 1px; padding-left: 10px;
  }
  .subtitle {
    position: absolute; left: 0; width: 816px; top: 418px; text-align: center;
    font-family: "Oswald", sans-serif; font-weight: 600; font-size: 29px; line-height: 1.2; color: var(--gold-dark);
  }
  .flourish {
    position: absolute; left: 246px; width: 324px; height: 42px;
    background: linear-gradient(90deg, transparent, var(--gold-light) 30%, var(--gold) 50%, var(--gold-light) 70%, transparent);
    opacity: 0.35; border-radius: 50%;
  }
  .flourish--upper { top: 470px; }
  .flourish--lower { top: 652px; }
  .dotted-rule {
    position: absolute; left: 186px; width: 446px; height: 5px;
    background: radial-gradient(circle, var(--gold) 2px, transparent 2.5px) 0 0 / 11.4px 5px repeat-x;
  }
  .dotted-rule--upper { top: 536px; }
  .dotted-rule--lower { top: 622px; }
  .dotted-rule--short { left: 309px; width: 182px; top: 833px; }
  .event-date {
    position: absolute; left: 0; width: 816px; top: 556px; text-align: center;
    font-weight: 800; font-size: 35px; line-height: 1.2; letter-spacing: 2px;
  }
  .event-time {
    position: absolute; left: 0; width: 816px; top: 698px; text-align: center;
    font-weight: 800; font-size: 52px; line-height: 1.1; letter-spacing: 1px;
  }
  .address {
    position: absolute; left: 0; width: 816px; top: 762px; text-align: center;
    font-style: italic; font-weight: 500; font-size: 26px; line-height: 32px; letter-spacing: 1.5px;
    color: var(--gold-dark); text-transform: uppercase;
  }
  .sparkle { position: absolute; border-radius: 50%; background: var(--gold); opacity: 0.7; }
</style>
</head>
<body>
<main class="flyer">
  <div class="photo" role="img" aria-label="Photo of a smiling therapist guiding a patient at a robotic therapy screen in a bright clinic"></div>
  <div class="ribbon ribbon--top-left" role="img" aria-label="Gold ribbon curl"></div>
  <div class="ribbon ribbon--top-right" role="img" aria-label="Gold ribbon with ribbon-cutting scissors"></div>
  <div class="ribbon ribbon--bottom-left" role="img" aria-label="Gold ribbon curl"></div>
  <div class="ribbon ribbon--bottom-right" role="img" aria-label="Gold ribbon curl"></div>

  <span class="sparkle" style="left:46px;top:204px;width:10px;height:10px"></span>
  <span class="sparkle" style="left:133px;top:81px;width:5px;height:5px"></span>
  <span class="sparkle" style="left:46px;top:472px;width:7px;height:7px"></span>
  <span class="sparkle" style="left:776px;top:40px;width:14px;height:14px"></span>
  <span class="sparkle" style="left:803px;top:296px;width:12px;height:12px"></span>
  <span class="sparkle" style="left:715px;top:431px;width:5px;height:5px"></span>
  <span class="sparkle" style="left:726px;top:572px;width:4px;height:4px"></span>
  <span class="sparkle" style="left:707px;top:683px;width:6px;height:6px"></span>
  <span class="sparkle" style="left:776px;top:725px;width:16px;height:16px"></span>
  <span class="sparkle" style="left:14px;top:720px;width:14px;height:14px"></span>
  <span class="sparkle" style="left:89px;top:622px;width:4px;height:4px"></span>

  <h1 class="headline headline--script gold-text">Grand</h1>

  <div class="brand">
    <span class="brand__mark"></span>
    <span class="brand__name">STELLAR MOTION THERAPY</span>
  </div>

  <h2 class="headline headline--block gold-text">OPENING</h2>
  <p class="subtitle">Robotic physical therapy Office</p>

  <div class="flourish flourish--upper" role="img" aria-label="Gold scroll ornament"></div>
  <div class="dotted-rule dotted-rule--upper"></div>
  <p class="event-date gold-text">THURSDAY,JUNE 1ST, 2023</p>
  <div class="dotted-rule dotted-rule--lower"></div>
  <div class="flourish flourish--lower" role="img" aria-label="Gold scroll ornament"></div>

  <p class="event-time gold-text">12-6PM</p>
  <address class="address">58274 Harlow Ave,<br>Bloomfield Hills, MI 48319</address>
  <div class="dotted-rule dotted-rule--short"></div>
</main>
</body>
</html>
```